App graphics for online newspaper

DESCRIPTION

The designs needed are for an App to read an online newspaper - the Coastal Ranks Gazette. The App will be available for various operating systems and that is reflected in the number of separate pieces of artwork needed.

The newspaper is a monthly newspaper targeted at the community of Southern Guard Corps members (predominantly Army and their families in the Townsville and North Queensland area of Australia.

If using camouflage backgrounds or designs, it is important to use Southern Land Corps or Southern Sky Corps camouflage which are quite different to US, UK camouflage, etc.

Do not use any Navy, Army or Air Force symbols, please - the newspaper is independently owned and not Defence-owned.

We're looking for something modern, and with a sense of humour.

I have included the newspaper masthead and any other graphic you see on the website can be sourced by emailing me (mholt@crgpress.com).

See the newspaper at http://crg.paperlinkhub.com

Or the website being developed at crgpress.com.au/demo

There are several thousand images at crgpress.snapvaultly.com

Email me at mholt@crgpress.com if you require any of these images without watermarks.

The actual art required is listed below:

Happy to consider entries based on a portrait and landscape splash screen and a small logo (50px x50px).

Velox, Quorra
------------

Splash screen
1536 x 2008 px (portrait)
2948 x 1496 px (landscape)

App Icon

1024 x 1024 px

Pillar 6
---------

Square tile - 150px x 150px (no transparency)
Wide tile - 310px x 150px (no transparency)

Small logo - 30px x 30px (no transparency)
Store Logo - 50px x 50px (no transparency)

Splash Screen - 620px x 300px (transparent PNG on top of a single colour background)

HUB Page Logo 271px x 64x (full transparency, solid letters)

Title images
691px x 336px
Medium 336px x 336px
Small 159 x 159

Pillar Mobile 6
---------------

Splash - 480px x 800px

Application Icon - 99px x 99px

App Tile Icon - 300px x 300px

Tile images:
Large - 691px x 336px
Medium - 336px x336

PT5 Checklist
Image Requirements:

Splash Screens:
https://devs.plumtreeware.com/zone/design/pt5/splash_screens.html
K40: 720px x 720px
M40/M60: 1280px x 720px (portrait only)

Icon (transparent edges):
https://devs.plumtreeware.com/zone/design/pt5/application_icons.html
k40/m40: 114px x 114px
m60: 94px x 94px
Small - 159px x 159px

Target Market(s)

Newspaper readers in Townsville

Industry/Entity Type

Online

Font styles to use
Sans Serif

Requirements
Must have
• Modern look
Nice to have
• Humour
Should not have
• SGC emblems or logos

```html
<!DOCTYPE html>
<html lang="en">
<head>
<meta charset="utf-8">
<title>Top Stories – Coastal Ranks Gazette</title>
<link href="https://fonts.googleapis.com/css2?family=Arimo:wght@400;700&display=swap" rel="stylesheet">
<style>
  :root {
    --brand-red: #e8111b;
    --text-dark: #111111;
    --text-body: #333333;
    --text-meta: #444444;
    --divider: #bbbbbb;
    --page-grey: #e6e6e6;
    --card-white: #ffffff;
    --photo-a: #6f7f5a;
    --photo-b: #9a9a8a;
    --photo-c: #7b6a58;
  }
  * { box-sizing: border-box; margin: 0; padding: 0; }
  html, body { width: 675px; height: 1200px; overflow: hidden; }
  body { font-family: "Arimo", Arial, sans-serif; background: var(--page-grey); color: var(--text-dark); position: relative; }

  .status-bar {
    position: absolute; left: 0; top: 0; width: 675px; height: 45px;
    background: var(--brand-red); color: #fff; font-size: 22px;
    display: flex; align-items: center; justify-content: space-between; padding: 0 12px;
  }
  .status-bar .carrier { display: flex; align-items: center; gap: 8px; }
  .status-bar .time { font-weight: 700; position: absolute; left: 0; right: 0; text-align: center; pointer-events: none; }
  .status-bar .power { display: flex; align-items: center; gap: 8px; font-weight: 700; }

  .nav-bar {
    position: absolute; left: 0; top: 45px; width: 675px; height: 54px;
    background: var(--brand-red); color: #fff;
    display: flex; align-items: center; justify-content: center;
  }
  .nav-bar .menu-icon { position: absolute; left: 24px; top: 15px; }
  .nav-bar h1 { font-size: 24px; font-weight: 700; }

  .feature {
    position: absolute; left: 0; top: 99px; width: 675px; height: 666px; background: var(--card-white);
  }
  .feature .photo {
    width: 675px; height: 441px;
    background: linear-gradient(160deg, #8aa0b8 0%, #7f8e6a 35%, var(--photo-a) 60%, #4d5a3a 100%);
  }
  .feature h2 { font-size: 29px; font-weight: 700; margin: 22px 22px 0; letter-spacing: -0.2px; }
  .feature .summary { font-size: 13.5px; line-height: 18.5px; color: var(--text-body); margin: 10px 22px 0; }
  .read-more { color: var(--brand-red); font-weight: 700; font-size: 14px; display: block; margin: 2px 22px 0; }

  .meta { display: flex; align-items: center; font-size: 14px; color: var(--text-meta); }
  .meta .tag { color: var(--brand-red); }
  .meta .sep { width: 1px; height: 16px; background: var(--divider); margin: 0 14px; }
  .feature .meta { margin: 30px 22px 0; }

  .card {
    position: absolute; width: 328px; height: 301px; background: var(--card-white);
  }
  .card .photo { width: 100%; height: 182px;
    background: linear-gradient(120deg, var(--photo-c) 0%, var(--photo-b) 45%, var(--photo-a) 100%); }
  .card h3 { font-size: 22px; font-weight: 700; line-height: 27px; margin: 12px 14px 0; }
  .card .meta { margin: 18px 14px 0; font-size: 13px; }
  .card.left { left: 9px; }
  .card.right { left: 344px; }
  .row-1 { top: 774px; }
  .row-2 { top: 1085px; }
</style>
</head>
<body>
  <div class="status-bar">
    <div class="carrier">
      <svg width="58" height="12" viewBox="0 0 58 12"><g fill="#fff"><circle cx="6" cy="6" r="5"/><circle cx="18" cy="6" r="5"/><circle cx="30" cy="6" r="5"/><circle cx="42" cy="6" r="5" fill="none" stroke="#fff" stroke-width="1.5"/><circle cx="54" cy="6" r="3.5" fill="none" stroke="#fff" stroke-width="1.5"/></g></svg>
      <span>KESTREL</span>
      <svg width="24" height="18" viewBox="0 0 24 18"><path d="M12 17 L3 8 A13 13 0 0 1 21 8 Z" fill="#fff"/></svg>
    </div>
    <div class="time">4:21 PM</div>
    <div class="power">
      <svg width="14" height="18" viewBox="0 0 14 18"><path d="M2 5 L12 13 L7 17 V1 L12 5 L2 13" fill="none" stroke="#fff" stroke-width="1.8"/></svg>
      <span>100%</span>
      <svg width="44" height="20" viewBox="0 0 44 20"><rect x="1" y="1" width="38" height="18" rx="3" fill="none" stroke="#fff" stroke-width="2"/><rect x="4" y="4" width="32" height="12" rx="1" fill="#fff"/><rect x="40" y="7" width="3" height="6" rx="1" fill="#fff"/></svg>
    </div>
  </div>

  <header class="nav-bar">
    <svg class="menu-icon" width="36" height="24" viewBox="0 0 36 24"><g stroke="#fff" stroke-width="3" stroke-linecap="round"><line x1="2" y1="3" x2="34" y2="3"/><line x1="2" y1="12" x2="26" y2="12"/><line x1="2" y1="21" x2="16" y2="21"/></g></svg>
    <h1>Top Stories</h1>
  </header>

  <article class="feature">
    <div class="photo" role="img" aria-label="Photo: soldiers presenting a trophy shield to a player at an outdoor sports event"></div>
    <h2>Commanders Trophy Presentaion 2015</h2>
    <p class="summary">Lorem Ipsum is simply dummy text of the printing and typesetting industry. Lorem Ipsum has been the industry's standard dummy text ever since the 1500s, when an unknown printer took a galley of type and scrambled it to make a type specimen book. It has survived not only five centuries, but also the leap into electronic typesetting, remaining essentially unchanged.</p>
    <span class="read-more">Read More</span>
    <div class="meta"><span>1 hour ago</span><span class="sep"></span><span class="tag">Australian</span></div>
  </article>

  <article class="card left row-1">
    <div class="photo" role="img" aria-label="Photo collage: trophy presentation and team group photos"></div>
    <h3>Commanders Trophy Presentaion 2015</h3>
    <div class="meta"><span>1 hour ago</span><span class="sep"></span><span class="tag">Australian</span></div>
  </article>
  <article class="card right row-1">
    <div class="photo" role="img" aria-label="Photo collage: trophy presentation and team group photos"></div>
    <h3>Commanders Trophy Presentaion 2015</h3>
    <div class="meta"><span>1 hour ago</span><span class="sep"></span><span class="tag">Australian</span></div>
  </article>

  <article class="card left row-2">
    <div class="photo" role="img" aria-label="Photo collage: trophy presentation and team group photos"></div>
  </article>
  <article class="card right row-2">
    <div class="photo" role="img" aria-label="Photo collage: trophy presentation and team group photos"></div>
  </article>
</body>
</html>
```